Pactwise - Training I Consulting I Review - Related to Contracts/Agreements

We provide legal services, we need a plattform to book video online trainings or local trainings classes and appointments (with calendar feature to select date and see availability at screen), payment over internet, legal document creation over webpage, videos will be produces in the next 3 - 4 moths so this is a place holder item. Participants for the Online trainings shall have a login in area with secured password. Appointments for local trainings and Consulting. Consider Outline in file attached. I can send you also a video with more explanation regarding the purpose.

Target Market(s)

Startup/scale up Software companies that intent to have an international business and need help with their contracts, to sell their products. Sales persons.

Industry/Entity Type

Legal

Coding

Coded - Design and coding required

Number of Pages Required

5+ page

Font styles to use
Serif
Sans Serif

Colors
000000
eeeeee
f5f5f5
ffffff
f8fcfd
3277b5
ecf7fb
cadf82
86cfc6

Requirements
Must have
• See file pactwise attached with outline. Moreover see here first starting point: https://moritz-ebbing.sitebuildr-demo.net/mysite-1 . Main inspiration comes from www.advisoryhub-demo.net from the log in area, see the outline in the file attached with the screen shots. At the end I need someone who can draft the full webpage and maintain it for a yearly fee. It must be simple and well structured layout. Lean. 1st landing page shall not scroll, 2 landing page only a little to see the testimonials and foster of page. There should be a Progress Bar to indicate the booking/selection process. Calendar booking. Easy fast booking.
• I like the colour mix, the feeling and the easy structor of:
• https://www.artpitch-demo.net/design/6374387or
• https://www.artpitch-demo.net/design/6372391 or https://www.artpitch-demo.net/design/6374366
• https://www.agencyfind-demo.net/en/web-design/belgium-be
• https://www.artpitch-demo.net/design/5896857
• https://www.artpitch-demo.net/design/5902173
• https://www.artpitch-demo.net/design/17197349
• https://www.artpitch-demo.net/design/5464461
• https://www.artpitch-demo.net/design/7180908
Nice to have
• page for evaluation and interview, see outline attached in the file with screen shots. Document upload.
Should not have
• many pictures, long scroll down pages on the 1st and 2nd ladding pages, many colours and forms. No need for news letter, search field, no need for links to Chatterly and other social media (except workNet).

```html
<!DOCTYPE html>
<html lang="en">
<head>
<meta charset="utf-8">
<title>Pactwise</title>
<link href="https://fonts.googleapis.com/css2?family=Barlow:wght@400;500;600&family=Arimo:wght@400;700&display=swap" rel="stylesheet">
<style>
:root{
  --blue:#3a5bb0;
  --ink:#111;
  --dark:#2d2d2d;
  --grey:#f1f1f1;
  --footer:#111;
  --white:#fff;
  --muted:#444;
}
*{margin:0;padding:0;box-sizing:border-box}
html,body{width:857px;height:1200px;overflow:hidden;background:var(--white)}
body{position:relative;font-family:"Arimo",Arial,sans-serif;color:var(--ink)}
.abs{position:absolute}
.head{font-family:"Barlow",Arial,sans-serif}
.topline{left:0;top:0;width:857px;height:2px;background:var(--blue)}
.logo{left:72px;top:30px;font:500 33px "Barlow",sans-serif;color:var(--ink);letter-spacing:-.3px}
.util{top:11px;font:400 14px "Barlow",sans-serif;color:var(--ink);display:flex;align-items:center;gap:5px}
.util.phone{left:559px;font-size:15px}
.util.login{left:684px;font-size:12.5px}
.sep{left:673px;top:11px;width:1px;height:16px;background:#555}
.nav{top:47px;left:390px;display:flex;gap:22px;font:400 12.5px "Barlow",sans-serif}
.nav a{color:var(--ink);text-decoration:none;position:relative}
.nav a.on{color:var(--blue)}
.nav a.on::before{content:"";position:absolute;left:0;right:0;top:-3px;height:2px;background:var(--blue)}
.hero{left:0;top:71px;width:857px;height:337px;background:linear-gradient(110deg,#3a3f48 0%,#6b7079 28%,#9aa0a8 45%,#5a6577 62%,#24324d 100%)}
.hero h1{position:absolute;top:131px;width:100%;text-align:center;font:500 25px "Barlow",sans-serif;color:#fff}
.hero p{position:absolute;top:170px;width:100%;text-align:center;font:500 25px "Barlow",sans-serif;color:#fff;letter-spacing:.2px}
.sectitle{width:857px;text-align:center;font:500 25px "Barlow",sans-serif;color:var(--dark)}
.sectitle span{color:var(--blue)}
.rule{width:27px;height:2px;background:#1f3a66;left:415px}
.service{width:200px;text-align:center}
.badge{width:88px;height:88px;border-radius:50%;border:4px solid #ddd;margin:0 auto;display:flex;align-items:center;justify-content:center}
.badge i{width:80px;height:80px;border-radius:50%;display:flex;align-items:center;justify-content:center;background:var(--dark)}
.badge.blue i{background:var(--blue)}
.service h3{margin-top:12px;font:500 14.5px "Barlow",sans-serif;color:var(--ink)}
.service h3.blue{color:var(--blue)}
.service p{margin-top:6px;font-size:9.6px;line-height:16px;color:var(--muted)}
.service a{display:inline-block;margin-top:9px;font:400 12px "Barlow",sans-serif;color:var(--ink)}
.service a.blue{color:var(--blue)}
.reviews{left:0;top:700px;width:857px;height:257px;background:var(--grey)}
.quote{left:155px;top:804px;width:530px;text-align:center;font-size:11.2px;line-height:20px;color:var(--ink)}
.qm{font:700 24px Georgia,serif;color:#999}
.who{top:876px;width:857px;text-align:center;font:500 13px "Barlow",sans-serif;color:var(--blue)}
.where{top:896px;width:857px;text-align:center;font-size:11px;color:var(--ink)}
.footer{left:0;top:957px;width:857px;height:205px;background:var(--footer);color:#fff}
.ftitle{font:400 14px "Barlow",sans-serif;color:#fff}
.ftitle::after{content:"";display:block;width:30px;height:1px;background:#555;margin-top:9px}
.links{list-style:none;font:400 10px "Barlow",sans-serif}
.links li{margin-bottom:10px;padding-left:9px;position:relative;line-height:12px}
.links li::before{content:"›";position:absolute;left:0;color:#666}
.crow{display:flex;align-items:flex-start;gap:10px;font-size:10.5px;line-height:15px}
.ico{width:15px;height:15px;border-radius:50%;background:var(--blue);flex:none;display:flex;align-items:center;justify-content:center}
.field{background:#fff;color:#555;font-size:7.5px;padding:0 9px;display:flex;align-items:center;width:151px;height:24px}
.submit{left:638px;top:1113px;width:63px;height:19px;background:var(--blue);color:#fff;font:600 11px "Barlow",sans-serif;display:flex;align-items:center;justify-content:center;border-radius:2px}
.bottom{left:0;top:1162px;width:857px;height:38px;background:var(--blue);color:#fff}
</style>
</head>
<body>
<div class="abs topline"></div>
<div class="abs logo">Pactwise</div>
<div class="abs util phone">
  <svg width="16" height="16" viewBox="0 0 16 16"><circle cx="8" cy="8" r="7" fill="none" stroke="#3a5bb0" stroke-width="1.3"/><path d="M6 4.5c-1 1.5-1 4.5 1.5 7l1-1.2-1-1.6 .8-.6-1-2.5z" fill="#3a5bb0"/></svg>
  123.456.7890
</div>
<div class="abs sep"></div>
<div class="abs util login">
  <svg width="22" height="14" viewBox="0 0 22 14"><path d="M1 4l5-3 5 2 5-2 5 3-3 5-5 4-5-3z" fill="#3a5bb0"/></svg>
  Partner Login
</div>
<nav class="abs nav">
  <a class="on" href="#">Home</a><a href="#">Refer Someone Services</a><a href="#">Reviews</a><a href="#">Our Team</a><a href="#">Contact Us</a>
</nav>

<section class="abs hero" role="img" aria-label="Photo of two business people shaking hands">
  <h1>Pactwise CONTRACTS</h1>
  <p>Contract Training.&nbsp; Contract Consulting.&nbsp; Contract Review</p>
</section>

<h2 class="abs sectitle" style="top:428px">Choose Your <span>Service</span></h2>
<div class="abs rule" style="top:469px"></div>

<div class="abs service" style="left:75px;top:498px">
  <div class="badge blue"><i><svg width="36" height="30" viewBox="0 0 36 30" fill="#fff"><rect x="12" y="2" width="22" height="14" fill="none" stroke="#fff" stroke-width="2"/><path d="M15 12l5-4 4 3 7-6" fill="none" stroke="#fff" stroke-width="1.6"/><circle cx="7" cy="6" r="3"/><rect x="3" y="10" width="8" height="8"/><circle cx="6" cy="22" r="2.3"/><circle cx="14" cy="22" r="2.3"/><circle cx="22" cy="22" r="2.3"/><circle cx="30" cy="22" r="2.3"/><rect x="2" y="25" width="32" height="5"/></svg></i></div>
  <h3 class="blue">Training</h3>
  <p>Lorem ipsum dolor sit amet lores ore<br>consectetuer adipiscing ...</p>
  <a class="blue" href="#">Book</a>
</div>
<div class="abs service" style="left:325px;top:498px">
  <div class="badge"><i><svg width="36" height="34" viewBox="0 0 36 34" fill="#fff"><circle cx="8" cy="5" r="3.5"/><circle cx="18" cy="5" r="3.5"/><circle cx="28" cy="5" r="3.5"/><rect x="3" y="11" width="6" height="12"/><rect x="27" y="11" width="6" height="12"/><rect x="11" y="14" width="14" height="4"/><rect x="15" y="18" width="6" height="13"/><rect x="5" y="23" width="8" height="3"/><rect x="23" y="23" width="8" height="3"/></svg></i></div>
  <h3>Consulting</h3>
  <p>Lorem ipsum dolor sit amet lores ore<br>consectetuer adipiscing ...</p>
  <a href="#">Appointment</a>
</div>
<div class="abs service" style="left:577px;top:498px">
  <div class="badge"><i><svg width="40" height="38" viewBox="0 0 40 38" fill="none" stroke="#fff" stroke-width="2"><rect x="2" y="2" width="36" height="34"/><line x1="2" y1="9" x2="38" y2="9"/><line x1="2" y1="14" x2="38" y2="14"/><rect x="6" y="18" width="12" height="14"/><rect x="22" y="18" width="12" height="14"/></svg></i></div>
  <h3>Template</h3>
  <p>Lorem ipsum dolor sit amet lores ore<br>consectetuer adipiscing ...</p>
  <a href="#">Request</a>
</div>

<section class="abs reviews"></section>
<h2 class="abs sectitle" style="top:735px">Customer <span>Reviews</span></h2>
<div class="abs rule" style="top:772px"></div>
<svg class="abs" style="left:88px;top:842px" width="20" height="40" viewBox="0 0 20 40"><path d="M18 1L2 20l16 19" fill="none" stroke="#999" stroke-width="1.2"/></svg>
<svg class="abs" style="left:736px;top:842px" width="20" height="40" viewBox="0 0 20 40"><path d="M2 1l16 19L2 39" fill="none" stroke="#999" stroke-width="1.2"/></svg>
<span class="abs qm" style="left:148px;top:793px">“</span>
<p class="abs quote">Lorem ipsum dolor sit amet, consectetuer adipiscing elit, sed diam nonummy nibh euismod tinciduntol ut laoreet dolore magna aliquam erat volutpat. Ut wisi enim ad minim veniam, quis nostrud exercimori mornkle tation ullamcorper suscipit lobortis nisl ut aliquip ex ea commodo consequat.</p>
<span class="abs qm" style="left:608px;top:845px">”</span>
<div class="abs who">Marla K.</div>
<div class="abs where">Fairview Bay, OR</div>

<footer class="abs footer">
  <div class="abs ftitle" style="left:72px;top:30px">Quick Links</div>
  <ul class="abs links" style="left:72px;top:69px;width:100px">
    <li>Home</li><li>Refer Someone<br>Services</li><li>Reviews</li><li>Our Team</li><li>Contact Us</li>
  </ul>
  <div class="abs ftitle" style="left:226px;top:30px">Contact Details</div>
  <div class="abs" role="img" aria-label="Faint world map" style="left:222px;top:75px;width:180px;height:88px;background:radial-gradient(ellipse,#2a2a2a 0%,#161616 70%,transparent 100%)"></div>
  <div class="abs crow" style="left:224px;top:68px"><span class="ico"><svg width="7" height="9" viewBox="0 0 7 9"><path d="M3.5 0a3.3 3.3 0 00-3.3 3.3C.2 5.8 3.5 9 3.5 9s3.3-3.2 3.3-5.7A3.3 3.3 0 003.5 0z" fill="#fff"/></svg></span><div><span style="font-size:12px">Pactwise</span><br><span style="font-size:10px">Street Name, City Name<br>State Zipcode</span></div></div>
  <div class="abs crow" style="left:224px;top:122px"><span class="ico"><svg width="8" height="8" viewBox="0 0 8 8"><path d="M1 0c-1 2 0 5 3 7l2-1-1-2-1 .5L2.5 2.3 3 1.5 2 0z" fill="#fff"/></svg></span><span>123.456.7890</span></div>
  <div class="abs crow" style="left:224px;top:156px"><span class="ico"><svg width="8" height="6" viewBox="0 0 8 6"><rect width="8" height="6" fill="#fff"/><path d="M0 0l4 3 4-3" fill="none" stroke="#3a5bb0"/></svg></span><span>inquiry@pactwise.com</span></div>

  <div class="abs ftitle" style="left:478px;top:32px">Quick Inquiry</div>
  <div class="abs field" style="left:478px;top:67px">First Name</div>
  <div class="abs field" style="left:478px;top:96px">Email Address</div>
  <div class="abs field" style="left:478px;top:123px">Last Name</div>
  <div class="abs field" style="left:478px;top:152px">Contact Number</div>
  <div class="abs field" style="left:633px;top:67px;height:80px;align-items:flex-start;padding-top:9px">Message</div>
</footer>
<div class="abs submit">SUBMIT</div>

<div class="abs bottom">
  <div class="abs" style="left:75px;top:14px;font:400 9.5px 'Barlow',sans-serif">Copyright © 2018 Pactwise. All Rights Reserved.</div>
  <div class="abs" style="left:681px;top:10px;font:500 14px 'Barlow',sans-serif">Follow Us</div>
  <div class="abs" aria-label="workNet" style="left:751px;top:7px;width:24px;height:24px;border-radius:50%;background:#fff"></div>
</div>
</body>
</html>
```